Need App for Impact Related Events

My app is to help with internal events. When you enter the prompted event code the next screen shows you everyone currently at the event. It will give you the ability to Start a conversation with someone you met at that event, or signal it is your turn to send a message. The next screen is a message thread with that person. I am looking for a design that incorporates the colors and ‘feel good’ emotion of our logo. I have pieced together a pretty good interpretation of what I’m looking for in the attached mockup by slicing and dicing designs. I also attached our logo mascot.Screens (see attached mockups)

Note 1: I do not like the picture on the screen used in screen one because it makes it seem like a dating app. I attached an alternative photo that can be used or present different ideas.

Note 2: On the login/signup screen (screen 2) I need an additional first and last name for login, you can try to fit this on one login screen or present a two step signup screen where that is presented in the second screen.

READ MOCKUP GUIDELINES UNDER Must Haves

Target Market(s)

People attending internal social impact events

Industry/Entity Type

Charity

Font styles to use
Sans Serif

Colors
86cfc6

Requirements
Must have
• Follow the screen mockups attached to project
• PLEASE READ
• I have provided a relatively close design of what I’m looking for in the mockups. Some screens need to be followed more closely to my design mockup than other. I have listed a guide below how how closely you should follow my mockup design exactly. Overall I would like to see some ideas of incorporating a few accent colors so it doesn’t appear SO Blue. I also attached some app inspiration designs I found from around the web
• Screen Mockup Guideline Follow %
• Screen 1: 65% - mostly on target, would like to see ways to make it not SO Blue and possibly creative places to add some explainer text describing the app
• Screen 2: 50% - general design idea is here, but more open
• Screen 3: 35% - a lot more room for design influence
• Screen 4: 70% - mostly on target, a little room for design influence/color scheme ideas
• Screen 5-6: 25% - a lot of room for design change/ideas/influence
• Screen 7-8: 80% - already very close to what I need, maybe open to slight sizing and color scheme ideas
• Screen 9: 15% - the most open for influence, only the general functionality of the screen is communicated here
Nice to have
• Please Read Mockup Guideline above. In large part I am looking for something to use some nice accent colors so it is not overwhelmingly blue and bring the whole design into a seamless style.
Should not have

```html
<!DOCTYPE html>
<html lang="en">
<head>
<meta charset="utf-8">
<title>Kindly Hive – App Screens</title>
<link rel="stylesheet" href="https://fonts.googleapis.com/css2?family=Nunito+Sans:wght@400;600;700&display=swap">
<style>
  :root {
    --bg: #2c1446;
    --white: #ffffff;
    --ink: #2b2f3a;
    --muted: #9aa1ad;
    --field: #f3f4f7;
    --line: #eceef2;
    --cyan: #3ccbdc;
    --teal-deep: #15888f;
    --violet: #6450f0;
    --violet-soft: #8d7cf6;
    --stripe-purple: #7a3be0;
    --magenta: #d63ce0;
    --coral: #e23a5a;
    --amber: #f2b33d;
    --mint: #5fe0c0;
    --navy: #3b4f93;
    --chat-bubble: #7a8399;
  }
  * { box-sizing: border-box; margin: 0; padding: 0; }
  html, body { width: 1200px; height: 1200px; overflow: hidden; }
  body {
    background: var(--bg);
    font-family: "Nunito Sans", sans-serif;
    color: var(--ink);
    position: relative;
  }

  /* decorative stripes */
  .stripe { position: absolute; width: 56px; border-radius: 28px; box-shadow: 0 24px 40px rgba(10,0,25,.45); }
  .stripe-cyan { left: 35px; top: -40px; height: 788px; background: var(--cyan); }
  .stripe-magenta { left: 280px; top: -40px; height: 788px; background: var(--magenta); }
  .stripe-purple { left: 158px; top: 522px; height: 720px; background: var(--stripe-purple); }
  .stripe-red { left: 402px; top: 522px; height: 720px; background: var(--coral); }

  /* screens */
  .screen {
    position: absolute;
    width: 186px;
    height: 380px;
    background: var(--white);
    border-radius: 18px;
    overflow: hidden;
    transform: scale(.75);
    transform-origin: 0 0;
    box-shadow: 0 20px 40px rgba(10,0,25,.35);
  }
  .screen > * { position: absolute; }
  .col-1 { left: 558px; } .col-2 { left: 776px; } .col-3 { left: 995px; }
  .row-1 { top: 77px; } .row-2 { top: 437px; } .row-3 { top: 796px; }

  .status { top: 8px; left: 12px; right: 12px; display: flex; justify-content: space-between; font-size: 6px; font-weight: 700; }
  .status .icons { display: flex; gap: 2px; align-items: center; }
  .status .icons i { display: block; width: 6px; height: 4px; background: currentColor; border-radius: 1px; }
  .back { left: 14px; top: 28px; font-size: 10px; color: var(--ink); }
  .title { left: 18px; font-size: 17px; font-weight: 600; line-height: 1.25; }
  .field {
    left: 18px; right: 18px; height: 20px; border-radius: 10px; background: var(--field);
    font-size: 5.5px; color: #b6bbc5; padding-left: 11px; line-height: 20px;
  }
  .btn {
    left: 18px; right: 18px; height: 22px; border-radius: 11px;
    font-size: 7px; font-weight: 700; text-align: center; line-height: 22px; letter-spacing: .3px;
  }
  .btn-cyan { background: var(--cyan); color: var(--white); }
  .link { left: 0; right: 0; text-align: center; font-size: 7px; text-decoration: underline; color: var(--ink); }
  .skyline {
    left: 0; right: 0; bottom: 0; height: 72px;
    background: linear-gradient(180deg, rgba(60,203,220,0) 0%, rgba(60,203,220,.18) 100%);
  }
  .mascot { left: 80px; top: 50px; width: 26px; height: 26px; border-radius: 50%; background: var(--cyan); }
  .card {
    left: 16px; right: 16px; top: 96px; height: 128px; border-radius: 6px;
    background: var(--violet); color: var(--white); padding: 12px;
  }
  .card > * { position: absolute; }
  .small { font-size: 5.5px; line-height: 1.45; }
  .dots { left: 12px; bottom: 12px; display: flex; gap: 3px; }
  .dots i { width: 3px; height: 3px; border-radius: 50%; background: rgba(255,255,255,.5); }
  .dots i.on { background: var(--white); }
  .round-btn { width: 20px; height: 20px; border-radius: 50%; color: var(--white); font-size: 9px; text-align: center; line-height: 20px; }

  /* welcome */
  .welcome-photo { inset: 0; background: linear-gradient(170deg, #5a4a44 0%, #3b3a3c 40%, #2c2f3a 70%, #1f2430 100%); }
  .welcome-shade { inset: 0; background: linear-gradient(180deg, rgba(20,20,40,0) 30%, rgba(20,20,40,.6) 100%); }
  .brand { top: 96px; left: 0; right: 0; text-align: center; color: var(--white); font-size: 12px; font-weight: 700; }
  .brand-mark { top: 58px; left: 80px; width: 26px; height: 26px; border-radius: 50%; background: var(--cyan); }

  /* signup */
  .accent-tab { right: 0; width: 14px; top: 100px; height: 128px; background: var(--cyan); border-radius: 10px 0 0 10px; }

  /* photo prompt */
  .teal-bg { inset: 0; background: linear-gradient(180deg, var(--cyan) 0%, #2bb3bf 55%, var(--teal-deep) 100%); }

  /* met list */
  .person { left: 14px; right: 14px; height: 40px; display: flex; align-items: center; border-bottom: 1px solid var(--line); }
  .avatar { width: 18px; height: 18px; border-radius: 50%; flex: none; }
  .person .who { margin-left: 8px; flex: 1; font-size: 6px; line-height: 1.35; }
  .person .who span { display: block; color: var(--muted); font-size: 5px; }
  .pill { width: 36px; height: 12px; border-radius: 6px; font-size: 4.5px; font-weight: 700; text-align: center; line-height: 12px; color: var(--white); }
  .pill-start { background: linear-gradient(90deg, var(--violet), var(--magenta)); }
  .pill-start-violet { background: var(--violet); }
  .pill-turn { background: var(--cyan); }
  .pill-note { background: var(--field); color: var(--muted); font-weight: 400; }
  .dropdown {
    left: 14px; right: 14px; height: 18px; border-radius: 5px; border: 1px solid var(--line);
    font-size: 5.5px; color: var(--muted); padding: 0 8px; display: flex; justify-content: space-between; align-items: center;
  }

  /* chat */
  .chat-header { top: 0; left: 0; right: 0; height: 40px; background: var(--white); box-shadow: 0 2px 6px rgba(0,0,0,.05); }
  .bubble { border-radius: 6px; font-size: 5.5px; line-height: 1.5; color: var(--white); padding: 6px 8px; }
  .chat-input {
    left: 10px; right: 10px; bottom: 12px; height: 20px; border-radius: 4px; border: 1px solid var(--line);
    font-size: 5.5px; color: var(--muted); padding: 0 8px; display: flex; justify-content: space-between; align-items: center;
  }

  /* settings */
  .label { left: 16px; font-size: 5px; color: var(--muted); }
  .value { left: 16px; font-size: 6.5px; }
  .event { left: 16px; right: 16px; height: 24px; border-bottom: 1px solid var(--line); display: flex; align-items: center; font-size: 6px; }
  .event i { width: 4px; height: 4px; border-radius: 50%; margin-left: 8px; }
  .event span { margin-left: auto; font-size: 4.5px; color: var(--muted); }
</style>
</head>
<body>

<div class="stripe stripe-cyan"></div>
<div class="stripe stripe-magenta"></div>
<div class="stripe stripe-purple"></div>
<div class="stripe stripe-red"></div>

<!-- Screen 1: Welcome -->
<section class="screen col-1 row-1">
  <div class="welcome-photo" role="img" aria-label="Photo of people enjoying a community event together"></div>
  <div class="welcome-shade"></div>
  <div class="status" style="color:var(--white)"><span>9:41</span><span class="icons"><i></i><i></i><i></i></span></div>
  <div class="brand-mark"></div>
  <div class="brand">Kindly Hive</div>
  <div style="top:182px;left:0;right:0;text-align:center;color:var(--white);font-size:19px;">Welcome</div>
  <p class="small" style="top:210px;left:18px;right:18px;text-align:center;color:var(--white);">Lorem ipsum dolor sit amet, consectetuer adipiscing elit. Aenean commodo ligula eget dolor. Aenean massa.</p>
  <div style="top:272px;left:0;right:0;text-align:center;color:var(--white);font-size:4.5px;font-weight:700;">CONTINUE WITH</div>
  <div class="btn btn-cyan" style="top:284px;left:12px;right:12px;">LOGIN NOW</div>
  <div class="btn" style="top:318px;left:12px;right:12px;background:rgba(40,48,70,.85);color:var(--white);">CREATE ACCOUNT</div>
</section>

<!-- Screen 2: Sign up -->
<section class="screen col-2 row-1">
  <div class="status"><span>9:41</span><span class="icons"><i></i><i></i><i></i></span></div>
  <div class="back">←</div>
  <div class="title" style="top:60px;">Sign Up</div>
  <div class="accent-tab"></div>
  <div class="field" style="top:104px;right:22px;">Your first name</div>
  <div class="field" style="top:138px;right:22px;">Your last name</div>
  <div class="field" style="top:172px;right:22px;">Email</div>
  <div class="field" style="top:206px;right:22px;">Password (6+ characters)</div>
  <div class="btn" style="top:246px;border:1px solid var(--line);color:var(--cyan);">SIGN UP</div>
  <div style="top:278px;left:0;right:0;text-align:center;font-size:6px;">Or, Signup with Linkup</div>
  <div class="btn" style="top:296px;background:var(--navy);color:var(--white);font-weight:400;">LINKUP</div>
  <p style="top:340px;left:14px;right:14px;text-align:center;font-size:5px;line-height:1.5;">By signing up, you agree to <span style="color:var(--cyan)">terms of use</span> and <span style="color:var(--cyan)">privacy policy</span>.</p>
</section>

<!-- Screen 3: Add a photo -->
<section class="screen col-3 row-1">
  <div class="teal-bg"></div>
  <div class="status" style="color:var(--white)"><span>9:41</span><span class="icons"><i></i><i></i><i></i></span></div>
  <div style="top:62px;left:0;right:0;text-align:center;color:var(--white);font-size:8px;font-weight:600;">Hi, Nora Ellis</div>
  <svg style="top:100px;left:73px;" width="40" height="40" viewBox="0 0 40 40" aria-hidden="true">
    <circle cx="18" cy="18" r="16" fill="none" stroke="#fff" stroke-width="1.5"/>
    <circle cx="18" cy="14" r="5" fill="#fff"/>
    <path d="M9 28c2-6 16-6 18 0" fill="#fff"/>
    <circle cx="30" cy="30" r="6" fill="#2bb3bf" stroke="#fff" stroke-width="1.2"/>
    <path d="M30 27v6M27 30h6" stroke="#fff" stroke-width="1.2"/>
  </svg>
  <div style="top:170px;left:0;right:0;text-align:center;color:var(--white);font-size:8px;font-weight:700;">Now, Add a Photo</div>
  <p class="small" style="top:186px;left:20px;right:20px;text-align:center;color:var(--white);">Lorem ipsum dolor sit amet, consectetuer adipiscing elit. Aenean commodo ligula eget dolor. Aenean massa.</p>
  <div class="btn" style="top:230px;left:12px;right:12px;background:var(--white);color:var(--cyan);">ADD A PHOTO</div>
  <div style="top:282px;left:0;right:0;text-align:center;color:var(--white);font-size:6.5px;font-weight:700;">SKIP FOR NOW</div>
</section>

<!-- Screen 4: Enter code -->
<section class="screen col-1 row-2">
  <div class="status"><span>9:41</span><span class="icons"><i></i><i></i><i></i></span></div>
  <div class="back">←</div>
  <div class="title" style="top:72px;font-size:14px;">Enter Location<br>Kind Code</div>
  <div class="field" style="top:150px;">Enter Code</div>
  <div class="btn btn-cyan" style="top:186px;">SUBMIT</div>
  <div class="link" style="top:240px;">Create a Kind Code</div>
  <div class="skyline" role="img" aria-label="Light cyan city skyline illustration"></div>
</section>

<!-- Screen 5: Name location -->
<section class="screen col-2 row-2">
  <div class="status"><span>9:41</span><span class="icons"><i></i><i></i><i></i></span></div>
  <div class="back">←</div>
  <div class="mascot"></div>
  <div class="card">
    <div style="top:10px;left:12px;right:12px;font-size:8.5px;line-height:1.3;">Give Your Location a name....</div>
    <p class="small" style="top:38px;left:12px;right:12px;">Lorem ipsum dolor sit amet, consectetuer adipiscing elit.</p>
    <div style="top:66px;left:12px;right:12px;height:14px;border-radius:7px;background:var(--white);color:#b6bbc5;font-size:5px;line-height:14px;padding-left:8px;">Location name (optional)</div>
    <div class="dots"><i class="on"></i><i></i></div>
    <div class="round-btn" style="right:10px;bottom:8px;background:var(--cyan);">→</div>
  </div>
  <div class="link" style="top:244px;">Get Your Code</div>
  <div class="skyline" role="img" aria-label="Light cyan city skyline illustration"></div>
</section>

<!-- Screen 6: Your code -->
<section class="screen col-3 row-2">
  <div class="status"><span>9:41</span><span class="icons"><i></i><i></i><i></i></span></div>
  <div class="back">←</div>
  <div class="mascot"></div>
  <div class="card">
    <div style="top:10px;left:12px;font-size:8.5px;">Your Kind Code</div>
    <div style="top:26px;left:0;right:0;text-align:center;font-size:11px;font-weight:700;">A1134UC7896P</div>
    <p class="small" style="top:50px;left:12px;right:12px;">Give this code to the people at your location or event to allow them to connect with each other - Kind of like Wifi password</p>
    <div class="dots"><i></i><i class="on"></i></div>
    <div class="round-btn" style="right:34px;bottom:8px;background:var(--violet-soft);">←</div>
    <div class="round-btn" style="right:10px;bottom:8px;background:var(--cyan);">→</div>
  </div>
  <div class="link" style="top:238px;">Manage in Settings</div>
  <div class="skyline" role="img" aria-label="Light cyan city skyline illustration"></div>
</section>

<!-- Screen 7: You've met -->
<section class="screen col-1 row-3">
  <div class="status"><span>9:41</span><span class="icons"><i></i><i></i><i></i></span></div>
  <div class="back">←</div>
  <div style="top:26px;right:16px;font-size:9px;color:var(--muted);">⚙</div>
  <div class="title" style="top:50px;font-size:15px;">You've Met</div>
  <div class="person" style="top:78px;"><div class="avatar" role="img" aria-label="Profile photo" style="background:#b9826a"></div><div class="who">Lena Brooks<span>Canada</span></div><div class="pill pill-start">START</div></div>
  <div class="person" style="top:123px;"><div class="avatar" role="img" aria-label="Profile photo" style="background:#c79a7e"></div><div class="who">Omar Whitfield<span>Canada</span></div><div class="pill pill-turn">YOUR TURN</div></div>
  <div class="person" style="top:168px;"><div class="avatar" role="img" aria-label="Profile photo" style="background:#4a3a34"></div><div class="who">Theo Hartley<span>Canada</span></div><div class="pill pill-start-violet">START</div></div>
  <div class="person" style="top:213px;"><div class="avatar" role="img" aria-label="Profile photo" style="background:#8fa6b8"></div><div class="who">Ravi Dalton<span>Canada</span></div><div class="pill pill-note">Great idea...</div></div>
  <div class="person" style="top:258px;"><div class="avatar" role="img" aria-label="Profile photo" style="background:#d2a679"></div><div class="who">Ines Moreau<span>Canada</span></div><div class="pill pill-note">Cool meeting...</div></div>
  <div class="person" style="top:303px;border:0;"><div class="avatar" role="img" aria-label="Profile photo" style="background:#7c8fb0"></div><div class="who">Bastien Lemaire<span>Canada</span></div><div class="pill pill-note">Good Speech...</div></div>
  <div class="dropdown" style="top:348px;"><span>Hidden (52)</span><span style="color:var(--ink)">⌄</span></div>
</section>

<!-- Screen 8: Chat -->
<section class="screen col-2 row-3">
  <div class="bubble" style="top:30px;left:18px;width:120px;height:20px;padding:11px 8px 0;background:var(--violet);border-radius:0 0 6px 6px;font-size:5px;line-height:1;">who is doing it.</div>
  <div class="chat-header"></div>
  <div class="status"><span>9:41</span><span class="icons"><i></i><i></i><i></i></span></div>
  <div class="back">←</div>
  <div style="top:26px;left:58px;display:flex;align-items:center;gap:4px;font-size:9px;"><span class="avatar" role="img" aria-label="Profile photo" style="width:10px;height:10px;background:var(--amber)"></span>Nora</div>
  <div style="top:26px;right:14px;font-size:8px;color:var(--muted);">⌕</div>
  <div class="avatar" role="img" aria-label="Profile photo" style="top:64px;right:12px;width:10px;height:10px;background:#4a3a34"></div>
  <div class="bubble" style="top:72px;left:40px;right:22px;background:var(--chat-bubble);">Remember that not getting what you want is sometimes a wonderful stroke of luck.</div>
  <div style="top:122px;left:0;right:0;text-align:center;font-size:4.5px;color:var(--muted);">YESTERDAY, 7:40 PM</div>
  <div class="avatar" role="img" aria-label="Profile photo" style="top:136px;left:14px;width:10px;height:10px;background:var(--amber)"></div>
  <div class="bubble" style="top:142px;left:18px;width:132px;background:var(--violet);">You can't use up creativity. The more</div>
  <div style="top:176px;left:20px;width:130px;height:130px;border-radius:4px;background:linear-gradient(180deg,#5a2a6a 0%,#c23a5e 45%,#e86a5a 60%,#2a1a2a 80%,#150c18 100%);" role="img" aria-label="Shared photo of a lone tree against a vivid sunset sky"></div>
  <div class="chat-input"><span>Say something ...</span><span style="font-size:9px;color:var(--ink)">+</span></div>
</section>

<!-- Screen 9: Settings -->
<section class="screen col-3 row-3">
  <div class="status"><span>9:41</span><span class="icons"><i></i><i></i><i></i></span></div>
  <div class="back">←</div>
  <div style="top:26px;right:16px;font-size:8px;color:var(--muted);">✎</div>
  <div class="title" style="top:50px;left:16px;font-size:15px;">Settings</div>
  <div class="avatar" role="img" aria-label="Profile photo" style="top:86px;left:16px;width:28px;height:28px;background:linear-gradient(135deg,var(--amber),#e08a4a)"></div>
  <div style="top:88px;left:52px;font-size:9px;">Nora Ellis</div>
  <div style="top:102px;left:52px;font-size:5.5px;color:var(--muted);">Ontario, Canada</div>
  <div class="label" style="top:132px;">Email Address</div>
  <div class="value" style="top:140px;">nora.ellis@mail.test</div>
  <div style="top:154px;left:16px;right:16px;height:1px;background:var(--line);"></div>
  <div class="label" style="top:162px;">Status</div>
  <div class="value" style="top:170px;">Want to make world a better place to live</div>
  <div style="top:184px;left:16px;right:16px;height:1px;background:var(--line);"></div>
  <div class="label" style="top:194px;">Events (26)</div>
  <div class="event" style="top:200px;">Meet &amp; Greet<i style="background:var(--coral)"></i><span>Sep, 21</span></div>
  <div class="event" style="top:224px;">Charity Event<i style="background:var(--magenta)"></i><span>Sep, 18</span></div>
  <div class="event" style="top:248px;">Meetings<i style="background:var(--mint)"></i><span>Sep, 15</span></div>
  <div class="event" style="top:272px;">Workshop<i style="background:var(--amber)"></i><span>Sep, 11</span></div>
  <div class="dropdown" style="top:348px;"><span>More (22)</span><span style="color:var(--ink)">⌄</span></div>
</section>

</body>
</html>
```